Healthy Vending Machine Business Flyer

A modorn design that represents our healthy vending machine business. We will attach a picture of the machine we want on the flyer along with our logo. We will also upload the wording we want on the flyer

Colors

Designer to choose colors to be used in the design.

Requirements
Must have
• Flyer wording
• Front of flyer:
• (Picture of vending machine on the front)
• Free healthy vending machines hit the Treasure Valley
• Keep your Employees happy & productive with healthy vending options at work
• • No Cost to Your Company
• • Remote tracking tells us when your favorite snacks are running low
• • Credit Card/Smartphone Payment Technology
• • Ability to Customize your Snacks and Drinks
• • Locally Owned and Operated
• • Delicious Healthy Options
• Back of flyer:
• Quillow Healthy Vending is a locally owned and operated company dedicated to making healthy snacks and drinks easily available for the Treasure Valley. We provide the latest in vending machine technology accepting credit cards, zenno pay, and nimbus wallet. State of the art inventory tracking tells us when your machine is running low so you're never out of your favorite drink or snack. We offer flexible stocking based on your companies needs and work with you on what items you want in the machine. Our goal is to give your employees and clients healthy options on the go
• To be considered for this FREE service for your business please visit: quillowhealthyvending.com
• Or call/email today:
• Phone: 555-201-4736
• Email: quillowhealthyvending@mailvex.com
Should not have
• Any Additional Fruit images besides what is on the machine image.

```html
<!DOCTYPE html>
<html lang="en">
<head>
<meta charset="utf-8">
<title>Quillow Healthy Vending Flyer</title>
<link href="https://fonts.googleapis.com/css2?family=Montserrat:wght@500;600;700&family=Nunito:wght@900&display=swap" rel="stylesheet">
<style>
  :root {
    --backdrop: #7d7d7d;
    --orange: #f47b12;
    --orange-light: #f9a21c;
    --green: #3f8c1a;
    --green-dark: #2d6e12;
    --white: #ffffff;
  }
  * { box-sizing: border-box; margin: 0; padding: 0; }
  html, body { width: 1200px; height: 877px; overflow: hidden; }
  body { background: var(--backdrop); font-family: "Montserrat", sans-serif; position: relative; }

  .flyer {
    position: absolute; top: 64px; width: 528px; height: 748px;
    overflow: hidden; background: var(--white);
    box-shadow: 0 4px 12px rgba(0,0,0,.35);
  }
  .flyer--front { left: 62px; }
  .flyer--back { left: 610px; }
  .flyer__shapes { position: absolute; inset: 0; }

  .fruit-backdrop {
    position: absolute; left: 0; top: 120px; width: 528px; height: 300px;
    background: radial-gradient(ellipse at 40% 55%, rgba(240,200,150,.55), rgba(255,255,255,0) 70%);
  }

  .headline {
    position: absolute; right: 36px; top: 34px; text-align: right;
    font-family: "Nunito", sans-serif; font-weight: 900; font-size: 27px; line-height: 32px;
    color: var(--white); text-shadow: 1px 2px 2px rgba(0,0,0,.35);
  }

  .brand {
    position: absolute; left: 34px; top: 172px; width: 290px;
    font-family: "Montserrat", sans-serif; font-weight: 700; font-size: 31px; line-height: 35px;
    color: var(--orange);
  }

  .machine-photo {
    position: absolute; border-radius: 3px;
    background: linear-gradient(90deg, #1d1d1d 0 58%, #c8321e 58%, #5fa12a 78%, #c8321e 100%);
    box-shadow: 4px 6px 10px rgba(0,0,0,.35);
  }
  .flyer--front .machine-photo { left: 256px; top: 246px; width: 262px; height: 456px; }
  .flyer--back .machine-photo { left: 334px; top: 168px; width: 164px; height: 284px; }

  .pitch {
    position: absolute; left: 37px; top: 420px; width: 212px;
    font-weight: 700; font-size: 16px; line-height: 21.5px; letter-spacing: -0.2px;
    color: var(--white); text-transform: uppercase;
  }
  .benefits { position: absolute; left: 36px; top: 544px; width: 200px; list-style: none; }
  .benefits li {
    display: flex; gap: 5px; font-weight: 700; font-size: 11.4px; line-height: 15px;
    color: var(--white); margin-bottom: 3.5px;
  }
  .benefits svg { flex: 0 0 11px; margin-top: 2px; }

  .about {
    position: absolute; left: 45px; top: 459px; width: 440px;
    font-weight: 500; font-size: 11.2px; line-height: 14.8px; color: var(--white);
    text-align: justify; text-align-last: center;
  }
  .cta-bubble {
    position: absolute; left: 48px; top: 600px; width: 432px; height: 58px;
    background: var(--white); border-radius: 24px 24px 0 0; padding: 8px 0 0 16px;
  }
  .cta-bubble::after {
    content: ""; position: absolute; left: 212px; bottom: -10px;
    border-left: 10px solid transparent; border-right: 10px solid transparent;
    border-top: 10px solid var(--white);
  }
  .cta-bubble__lead { font-weight: 500; font-size: 11.6px; color: var(--green); }
  .cta-bubble__url { font-weight: 600; font-size: 23px; line-height: 28px; color: var(--green); }
  .contact {
    position: absolute; left: 0; top: 675px; width: 528px; text-align: center; color: var(--white);
  }
  .contact__lead { font-weight: 500; font-size: 13px; line-height: 17px; }
  .contact__details { font-weight: 700; font-size: 11.5px; line-height: 18px; }
</style>
</head>
<body>

<section class="flyer flyer--front">
  <svg class="flyer__shapes" width="528" height="748" viewBox="0 0 528 748">
    <defs>
      <linearGradient id="orangeTop" x1="0" y1="0" x2="1" y2="0">
        <stop offset="0" stop-color="#f9a21c"/><stop offset="1" stop-color="#f06a0d"/>
      </linearGradient>
      <linearGradient id="greenBase" x1="0" y1="0" x2="0" y2="1">
        <stop offset="0" stop-color="#4a9a1f"/><stop offset="1" stop-color="#2d6e12"/>
      </linearGradient>
    </defs>
    <path d="M0 0 H528 V232 C420 130 220 60 0 50 Z" fill="url(#orangeTop)"/>
    <path d="M470 0 H528 V30 Z" fill="#ffffff"/>
    <path d="M500 0 H528 V14 Z" fill="#3f8c1a"/>
    <path d="M0 380 C160 330 360 300 528 290 V748 H0 Z" fill="url(#greenBase)"/>
    <path d="M310 748 C250 600 270 430 420 300" fill="none" stroke="#ffffff" stroke-width="10"/>
  </svg>
  <div class="fruit-backdrop" role="img" aria-label="Faded background photo of fresh fruit"></div>
  <h1 class="headline">Free healthy vending<br>machines hit the<br>Treasure<br>Valley</h1>
  <div class="brand">Quillow Healthy<br>Vending</div>
  <div class="machine-photo" role="img" aria-label="Photo of the healthy vending machine with snacks, drinks and a fruit side wrap"></div>
  <h2 class="pitch">Keep your employees<br>happy &amp; productive<br>with healthy<br>vending options<br>at work</h2>
  <ul class="benefits">
    <li><svg width="11" height="11" viewBox="0 0 11 11"><circle cx="5.5" cy="5.5" r="4.7" fill="none" stroke="#fff" stroke-width="1.1"/><path d="M3 5.7 L4.8 7.4 L8 3.9" fill="none" stroke="#fff" stroke-width="1.2"/></svg>No Cost to Your Company</li>
    <li><svg width="11" height="11" viewBox="0 0 11 11"><circle cx="5.5" cy="5.5" r="4.7" fill="none" stroke="#fff" stroke-width="1.1"/><path d="M3 5.7 L4.8 7.4 L8 3.9" fill="none" stroke="#fff" stroke-width="1.2"/></svg>Remote tracking tells us when your favorite snacks are running low</li>
    <li><svg width="11" height="11" viewBox="0 0 11 11"><circle cx="5.5" cy="5.5" r="4.7" fill="none" stroke="#fff" stroke-width="1.1"/><path d="M3 5.7 L4.8 7.4 L8 3.9" fill="none" stroke="#fff" stroke-width="1.2"/></svg>Credit Card/Smartphone Payment Technology</li>
    <li><svg width="11" height="11" viewBox="0 0 11 11"><circle cx="5.5" cy="5.5" r="4.7" fill="none" stroke="#fff" stroke-width="1.1"/><path d="M3 5.7 L4.8 7.4 L8 3.9" fill="none" stroke="#fff" stroke-width="1.2"/></svg>Ability to Customize your Snacks and Drinks</li>
    <li><svg width="11" height="11" viewBox="0 0 11 11"><circle cx="5.5" cy="5.5" r="4.7" fill="none" stroke="#fff" stroke-width="1.1"/><path d="M3 5.7 L4.8 7.4 L8 3.9" fill="none" stroke="#fff" stroke-width="1.2"/></svg>Locally Owned and Operated</li>
    <li><svg width="11" height="11" viewBox="0 0 11 11"><circle cx="5.5" cy="5.5" r="4.7" fill="none" stroke="#fff" stroke-width="1.1"/><path d="M3 5.7 L4.8 7.4 L8 3.9" fill="none" stroke="#fff" stroke-width="1.2"/></svg>Delicious Healthy Options</li>
  </ul>
</section>

<section class="flyer flyer--back">
  <svg class="flyer__shapes" width="528" height="748" viewBox="0 0 528 748">
    <defs>
      <linearGradient id="orangeTopBack" x1="0" y1="0" x2="1" y2="0">
        <stop offset="0" stop-color="#f9a21c"/><stop offset="1" stop-color="#f06a0d"/>
      </linearGradient>
      <linearGradient id="greenBaseBack" x1="0" y1="0" x2="0" y2="1">
        <stop offset="0" stop-color="#4a9a1f"/><stop offset="1" stop-color="#2d6e12"/>
      </linearGradient>
    </defs>
    <path d="M0 0 H528 V232 C420 130 220 60 0 50 Z" fill="url(#orangeTopBack)"/>
    <path d="M470 0 H528 V30 Z" fill="#ffffff"/>
    <path d="M500 0 H528 V14 Z" fill="#3f8c1a"/>
    <path d="M0 380 C160 330 360 300 528 290 V748 H0 Z" fill="url(#greenBaseBack)"/>
  </svg>
  <div class="fruit-backdrop" role="img" aria-label="Faded background photo of fresh fruit"></div>
  <h1 class="headline">Free healthy vending<br>machines hit the<br>Treasure<br>Valley</h1>
  <div class="brand">Quillow Healthy<br>Vending</div>
  <div class="machine-photo" role="img" aria-label="Angled photo of the healthy vending machine with fruit side wrap"></div>
  <p class="about">Quillow Healthy Vending is a locally owned and operated company dedicated to making healthy snacks and drinks easily available for the Treasure Valley. We provide the latest in vending machine technology accepting credit cards, zenno pay, and nimbus wallet. State of the art inventory tracking tells us when your machine is running low so you're never out of your favorite drink or snack. We offer flexible stocking based on your companies needs and work with you on what items you want in the machine. Our goal is to give your employees and clients healthy options on the go.</p>
  <div class="cta-bubble">
    <p class="cta-bubble__lead">To be considered for this FREE service for your business please</p>
    <p class="cta-bubble__url">visit: quillowhealthyvending.com</p>
  </div>
  <div class="contact">
    <p class="contact__lead">Or call/email today:</p>
    <p class="contact__details">Ph: 555-201-4736 | Email: quillowhealthyvending@mailvex.com</p>
  </div>
</section>

</body>
</html>
```